Postcard bar mitzvah invitations

I'm looking for glossy postcards which which contain information for my son's bar mitzvah - the time and place of the service, that it will be followed by a luncheon, the time and place of the party, and how to RSVP.

```html
<!DOCTYPE html>
<html lang="en">
<head>
<meta charset="utf-8">
<title>Bar Mitzvah Postcard – Jacob</title>
<link rel="stylesheet" href="https://fonts.googleapis.com/css2?family=Cormorant+Garamond:ital,wght@0,500;0,600;1,500&family=Sorts+Mill+Goudy&display=swap">
<style>
  :root {
    --paper: #ffffff;
    --ink: #3a3a3a;
    --mint: #7fcdb4;
    --mint-soft: #a9dfcc;
    --mint-ghost: rgba(127, 205, 180, 0.16);
    --frame: #5cc6de;
    --frame-back: #3db8c9;
    --white-ghost: rgba(255, 255, 255, 0.2);
  }
  * { box-sizing: border-box; margin: 0; padding: 0; }
  html, body { width: 1200px; height: 927px; overflow: hidden; background: var(--paper); }
  .sheet { position: relative; width: 1200px; height: 927px; font-family: "Sorts Mill Goudy", serif; color: var(--ink); }

  .side-label { position: absolute; top: 116px; font-size: 17px; color: #222; font-family: "Sorts Mill Goudy", serif; }
  .side-label--front { left: 55px; }
  .side-label--back { left: 550px; }

  /* Front of card */
  .card-front {
    position: absolute; left: 55px; top: 166px; width: 465px; height: 601px;
    border: 1px solid var(--frame); background: var(--paper); overflow: hidden;
  }
  .tefillin-art {
    position: absolute; left: 165px; top: 28px; width: 136px; height: 80px;
    background: linear-gradient(135deg, var(--mint-soft), var(--mint)); border-radius: 10px 10px 16px 16px;
  }
  .line {
    position: absolute; left: 0; width: 100%; height: 22px; line-height: 22px;
    text-align: center; font-size: 15.5px; letter-spacing: 1.2px; font-variant: small-caps;
    white-space: nowrap;
  }
  .line--lower { font-variant: all-small-caps; font-size: 17px; }
  .honoree, .hosts {
    position: absolute; left: 0; width: 100%; text-align: center;
    font-family: "Cormorant Garamond", serif; font-style: italic; font-weight: 500;
    color: var(--mint); white-space: nowrap;
  }
  .honoree { top: 132px; font-size: 50px; line-height: 56px; }
  .honoree-ghost {
    position: absolute; left: 168px; top: 118px; font-size: 74px; line-height: 80px;
    font-family: "Cormorant Garamond", serif; font-style: italic; color: var(--mint-ghost);
    transform: rotate(-6deg); white-space: nowrap;
  }
  .hosts { top: 346px; font-size: 29px; line-height: 34px; }
  .divider-dots { position: absolute; left: 0; width: 100%; top: 461px; text-align: center; color: var(--mint); font-size: 10px; letter-spacing: 6px; }

  /* Back of card */
  .card-back {
    position: absolute; left: 550px; top: 234px; width: 600px; height: 463px;
    background: var(--mint); border: 1px solid var(--frame-back); overflow: hidden;
  }
  .return-address {
    position: absolute; left: 14px; top: 12px; color: var(--paper);
    font-size: 15.5px; line-height: 22.5px; letter-spacing: 1.3px; font-variant: small-caps;
  }
  .monogram-letter {
    position: absolute; left: 6px; top: 20px; font-family: "Cormorant Garamond", serif;
    font-weight: 500; font-size: 470px; line-height: 470px; color: var(--white-ghost);
  }
  .monogram-name {
    position: absolute; left: 14px; top: 226px; font-family: "Cormorant Garamond", serif;
    font-style: italic; font-size: 82px; line-height: 90px; color: var(--white-ghost);
  }
  .address-window {
    position: absolute; left: 273px; top: 163px; width: 274px; height: 137px;
    background: var(--paper); border-radius: 17px;
  }
  .address-prompt {
    position: absolute; left: 277px; top: 162px; font-family: "Cormorant Garamond", serif;
    font-style: italic; font-size: 34px; line-height: 40px; color: var(--mint-soft);
  }
</style>
</head>
<body>
<main class="sheet">
  <span class="side-label side-label--front">Front</span>
  <span class="side-label side-label--back">Back</span>

  <section class="card-front">
    <div class="tefillin-art" role="img" aria-label="Illustration of a pair of tefillin with straps"></div>
    <div class="honoree-ghost" aria-hidden="true">Jacob</div>
    <div class="line" style="top:113px">Please join us at the Bar Mitzvah of our dear son</div>
    <div class="honoree">Jacob</div>
    <div class="line" style="top:186px">on Saturday, June Thirteenth</div>
    <div class="line" style="top:209px">Two Thousand Fifteen</div>
    <div class="line" style="top:231px">at ten-thirty am</div>
    <div class="line" style="top:257px">Temple Beth Shalom</div>
    <div class="line" style="top:280px">2280 Maple Hill Road</div>
    <div class="line" style="top:302px">Cedar Falls, Ohio 44099</div>
    <div class="line" style="top:330px">Looking forward to greeting you,</div>
    <div class="hosts">Miriam and Joel Adler</div>
    <div class="line" style="top:382px">Please RSVP by May 31st</div>
    <div class="line line--lower" style="top:404px">adlerfam22@example.com -or- 216-555-0142</div>
    <div class="line" style="top:431px">Light lunch following bar mitzvah</div>
    <div class="divider-dots" aria-hidden="true">◆◆◆</div>
    <div class="line" style="top:484px">Celebration continues at Play Zone</div>
    <div class="line" style="top:506px">418 Ridge Avenue</div>
    <div class="line" style="top:529px">Brookfield, Ohio 44077</div>
    <div class="line" style="top:551px">4:00 pm to 8:00 pm</div>
  </section>

  <section class="card-back">
    <div class="monogram-letter" aria-hidden="true">J</div>
    <div class="monogram-name" aria-hidden="true">Jacob</div>
    <address class="return-address" style="font-style:normal">
      The Adlers<br>
      2280 Maple Hill Rd<br>
      Cedar Falls, OH 44099
    </address>
    <div class="address-window"></div>
    <div class="address-prompt">To:</div>
  </section>
</main>
</body>
</html>
```